Group Medical Practice needs stationery, business cards etc. designed

We need stationery designed for a multisite practice that offers primary medical, dental and behavioral healthcare. We would like a design that is consistent for letterhead, business cards, Microsoft Outlook stationery etc. We have attached our new logo design.

Business

```html
<!DOCTYPE html>
<html lang="en">
<head>
<meta charset="utf-8">
<title>Cedar Ridge Health Services – Envelope</title>
<link href="https://fonts.googleapis.com/css2?family=Arimo:wght@400;700&display=swap" rel="stylesheet">
<style>
  :root {
    --canvas: #d6d6d6;
    --paper: #ffffff;
    --leaf: #8cc63f;
    --brand-blue: #1b75bc;
    --ink: #1e1e1e;
    --window: #efefef;
  }
  * { margin: 0; padding: 0; box-sizing: border-box; }
  html, body { width: 1200px; height: 1000px; overflow: hidden; }
  body {
    background: var(--canvas);
    font-family: "Arimo", Arial, sans-serif;
    color: var(--ink);
    position: relative;
  }
  .envelope {
    position: absolute;
    left: 60px;
    width: 1075px;
    background: var(--paper);
  }
  .envelope--back { top: 20px; height: 468px; }
  .envelope--front { top: 519px; height: 465px; }

  .flap { position: absolute; left: 0; top: 0; width: 1075px; height: 230px; }
  .flap-name {
    position: absolute;
    left: 0; right: 0; top: 128px;
    text-align: center;
    color: var(--paper);
    font-weight: 700;
    font-size: 20px;
    letter-spacing: 1px;
  }
  .back-web {
    position: absolute;
    left: 0; right: 0; top: 440px;
    text-align: center;
    font-size: 15px;
  }

  .brand {
    position: absolute;
    left: 28px; top: 82px;
    display: flex; align-items: center; gap: 10px;
  }
  .brand-dot { width: 14px; height: 14px; border-radius: 50%; background: var(--leaf); }
  .brand-name {
    color: var(--brand-blue);
    font-weight: 700;
    font-size: 22px;
    letter-spacing: 0.5px;
  }

  .address-window {
    position: absolute;
    left: 489px; top: 192px;
    width: 487px; height: 192px;
    border-radius: 22px;
    background: var(--window);
  }

  .contact { position: absolute; left: 28px; top: 322px; list-style: none; font-size: 12.5px; line-height: 16px; }
  .contact li { display: flex; align-items: flex-start; gap: 6px; }
  .contact svg { width: 14px; height: 14px; flex: none; margin-top: 1px; fill: var(--leaf); }
  .contact .gap { margin-top: 10px; }
</style>
</head>
<body>
  <section class="envelope envelope--back">
    <svg class="flap" viewBox="0 0 1075 230" aria-hidden="true">
      <path d="M0 0 H1075 L1070 40 Q1062 68 1030 78 L700 182 Q537 228 375 182 L45 78 Q13 68 5 40 Z" fill="var(--leaf)"/>
    </svg>
    <div class="flap-name">Cedar Ridge Health Services</div>
    <p class="back-web">www.cedarridgehealth.com</p>
  </section>

  <section class="envelope envelope--front">
    <div class="brand">
      <span class="brand-dot"></span>
      <span class="brand-name">Cedar Ridge Health Services</span>
    </div>

    <div class="address-window"></div>

    <ul class="contact">
      <li>
        <svg viewBox="0 0 14 14"><path d="M7 0a5 5 0 0 0-5 5c0 3.5 5 9 5 9s5-5.5 5-9a5 5 0 0 0-5-5zm0 7a2 2 0 1 1 0-4 2 2 0 0 1 0 4z"/></svg>
        <span>42 Maple Grove Road Ste 210<br>Laurel Hollow, Virginia 24019</span>
      </li>
      <li class="gap">
        <svg viewBox="0 0 14 14"><path d="M3 1l2.5 3-1.5 1.5a8 8 0 0 0 4.5 4.5L10 8.5l3 2.5-1.5 2.5C6 13 1 8 .5 2.5z"/></svg>
        <span>0000 000 000</span>
      </li>
      <li>
        <svg viewBox="0 0 14 14"><rect x="3" y="1" width="8" height="4"/><rect x="1" y="6" width="12" height="5" rx="1"/><rect x="3" y="11" width="8" height="2"/></svg>
        <span>0000 000 000</span>
      </li>
      <li class="gap">
        <svg viewBox="0 0 14 14"><rect x="1" y="3" width="12" height="8" rx="1"/></svg>
        <span>info@cedarridgehealth.com</span>
      </li>
      <li>
        <svg viewBox="0 0 14 14"><circle cx="7" cy="7" r="6"/><path d="M1 7h12M7 1c-3 3-3 9 0 12M7 1c3 3 3 9 0 12" stroke="#fff" stroke-width="1" fill="none"/></svg>
        <span>www.cedarridgehealth.com</span>
      </li>
    </ul>
  </section>
</body>
</html>
```